Sundial Bail Bonds Signboard Ad

I need a signboard ad that will be posted at a jail. We are a bail bond company and we bail people out of jail. The inmate/customer will call our company when they see our signboard ad posted inside a jail. The goal of the signboard ad is to get the attention of a person in custody and to stand out from the competition. The signboard ad is about 5x7. Open to any colors that will make it stand out. The content of the signboard ad must have "Sundial Bail Bonds" and our company phone number: (555) 318-2746. We want to emphasize we can get them out of jail quick and fast, was thinking maybe a catch phrase of "Sundial outta Jail" or "Sundial to Freedom". We don't have a logo. I will upload an attachment to show what the competition looks like. As you will see in the upload, my ad will go along with my competition. Also, I'm open to any creative ideas that will make my signboard ad stand out. Thank You.

Target Market(s)

People in jail.

Requirements
Must have
• Sundial Bail Bonds

(555) 318-2746
Nice to have
• I'm open to catch phrases that will get attention, for example "Sundial outta Jail" or "Sundial to Freedom". I do not have a company logo, if you can create a company logo, would be nice, was thinking an image of a rocket blasting off, The name of company is Sundial Bail Bonds.

```html
<!DOCTYPE html>
<html lang="en">
<head>
<meta charset="utf-8">
<title>Sundial Bail Bonds – Signboard</title>
<link rel="stylesheet" href="https://fonts.googleapis.com/css2?family=Roboto+Condensed:ital,wght@0,700;1,900&family=Russo+One&display=swap">
<style>
  :root {
    --carbon: #141414;
    --carbon-light: #262626;
    --signal-yellow: #fdee1c;
    --alert-red: #d40000;
    --deep-red: #8c0000;
    --paper-white: #ffffff;
    --ink: #111111;
    --silver-light: #ffffff;
    --silver-dark: #b4b4b4;
  }
  html, body {
    margin: 0;
    padding: 0;
    width: 1200px;
    height: 864px;
    overflow: hidden;
    background: var(--paper-white);
  }
  .signboard {
    display: block;
    width: 1200px;
    height: 864px;
  }
  .company-name {
    font-family: "Russo One", sans-serif;
    fill: var(--paper-white);
  }
  .company-name-first { font-size: 150px; }
  .company-name-second { font-size: 130px; }
  .phone-number {
    font-family: "Roboto Condensed", sans-serif;
    font-weight: 700;
    font-size: 160px;
    fill: var(--alert-red);
  }
  .tagline {
    font-family: "Roboto Condensed", sans-serif;
    font-style: italic;
    font-weight: 900;
    font-size: 138px;
    fill: url(#silver-metal);
    filter: drop-shadow(4px 4px 0 var(--ink));
  }
</style>
</head>
<body>
<svg class="signboard" viewBox="0 0 1200 864" xmlns="http://www.w3.org/2000/svg" role="img" aria-label="Sundial Bail Bonds signboard: call (555) 318-2746, Sundial outta Jail">
  <defs>
    <linearGradient id="carbon-bg" x1="0" y1="0" x2="1" y2="1">
      <stop offset="0" stop-color="var(--carbon-light)"/>
      <stop offset="1" stop-color="var(--carbon)"/>
    </linearGradient>
    <linearGradient id="silver-metal" x1="0" y1="0" x2="0" y2="1">
      <stop offset="0" stop-color="var(--silver-light)"/>
      <stop offset="1" stop-color="var(--silver-dark)"/>
    </linearGradient>
    <linearGradient id="red-sweep" x1="0" y1="0" x2="1" y2="0">
      <stop offset="0" stop-color="var(--deep-red)"/>
      <stop offset="0.45" stop-color="var(--alert-red)"/>
      <stop offset="0.8" stop-color="#c00000"/>
      <stop offset="1" stop-color="var(--deep-red)"/>
    </linearGradient>
  </defs>

  <!-- upper panel -->
  <rect class="panel-carbon" x="0" y="0" width="1200" height="449" fill="url(#carbon-bg)"/>
  <polygon class="accent-yellow-top" points="512,0 1200,0 1200,199" fill="var(--signal-yellow)"/>
  <polygon class="accent-red-left" points="0,378 0,449 246,449" fill="var(--deep-red)"/>
  <polygon class="accent-red-left-inner" points="0,378 92,380 246,449 180,449" fill="#b00000"/>

  <!-- company name -->
  <text class="company-name company-name-first" x="600" y="220" text-anchor="middle" textLength="860" lengthAdjust="spacingAndGlyphs">SUNDIAL</text>
  <text class="company-name company-name-second" x="600" y="378" text-anchor="middle" textLength="940" lengthAdjust="spacingAndGlyphs">BAIL BONDS</text>

  <!-- phone band -->
  <rect class="phone-band" x="0" y="449" width="1200" height="189" fill="var(--paper-white)"/>
  <text class="phone-number" x="600" y="600" text-anchor="middle" textLength="940" lengthAdjust="spacingAndGlyphs">(555) 318-2746</text>

  <!-- lower panel -->
  <rect class="panel-red" x="0" y="638" width="1200" height="226" fill="url(#red-sweep)"/>
  <polygon class="accent-carbon-right" points="907,638 1200,638 1200,723" fill="var(--carbon)"/>
  <polygon class="accent-yellow-bottom" points="0,772 322,864 0,864" fill="var(--signal-yellow)"/>
  <g transform="translate(600 790) skewX(-10)">
    <text class="tagline" x="0" y="0" text-anchor="middle" textLength="960" lengthAdjust="spacingAndGlyphs">SUNDIAL OUTTA JAIL</text>
  </g>
</svg>
</body>
</html>
```